TR Ingotvale Corporate Letterhead

I have a corporate logo (uploaded). However, it may not be high enough quality for printing purposes, so the logo may need some work. I have a sample of letterhead (uploaded) that we currently use for electronic purposes only. The new design for letterhead does NOT need to look like the current electronic version -- in fact, I would prefer it doesn't. Additionally, I would like to be able to print this through pelkaprint.com. If your design includes something on the reverse side of the paper, that's okay (even cool!) -- pelkaprint.com can easily handle the printing of this. In summary I would like a letterhead design for print purposes, as well as an electronic version of the letterhead (to replace our current version) that can be used with Microsoft Word. Also, if you want to see how the logo on our website looks, go to www.tringotvale.com.

Requirements
Must have
• At least the front side of a letterhead design using our current logo. A backside of the letterhead is optional. Must be able to print through pelkaprint.com. Also must have an electronic version of the final design to use with Microsoft Word. Also, if the logo I uploaded isn't high enough quality, the logo will need to be enhanced for printing purposes. The color that I picked on ArtHively's color wheel may not be the correct blue, so feel free to change that if necessary. Also, the address and website address can be in a contrasting color chosen by the designer.
Nice to have
• I like original ideas/designs. So have fun with it!
Should not have
• Colors that are not in our current logo. If you would like to view it on our website, got to www.tringotvale.com

```html
<!DOCTYPE html>
<html lang="en">
<head>
<meta charset="UTF-8">
<title>TR Ingotvale Letterhead</title>
<link href="https://fonts.googleapis.com/css2?family=Open+Sans:wght@600&display=swap" rel="stylesheet">
<style>
  :root {
    --brand-blue: #2370b6;
    --footer-blue: #2a6db3;
    --band-gray: #9a9a9a;
    --paper: #ffffff;
  }
  * { margin: 0; padding: 0; box-sizing: border-box; }
  html, body { width: 848px; height: 1200px; overflow: hidden; background: var(--paper); }
  .letterhead {
    position: relative;
    width: 848px;
    height: 1200px;
    background: var(--paper);
  }
  .brand-name {
    position: absolute;
    left: 68px;
    top: 58px;
    font-family: "Open Sans", Arial, sans-serif;
    font-weight: 600;
    font-size: 42px;
    line-height: 1;
    color: var(--brand-blue);
    white-space: nowrap;
  }
  .contact-line {
    position: absolute;
    left: 67px;
    top: 1152px;
    font-family: "Open Sans", Arial, sans-serif;
    font-weight: 600;
    font-size: 14px;
    line-height: 1;
    color: var(--footer-blue);
    white-space: nowrap;
  }
  .band-gray {
    position: absolute;
    left: 0;
    top: 1179px;
    width: 848px;
    height: 10px;
    background: var(--band-gray);
  }
  .band-blue {
    position: absolute;
    left: 0;
    top: 1189px;
    width: 848px;
    height: 11px;
    background: var(--brand-blue);
  }
</style>
</head>
<body>
  <div class="letterhead">
    <div class="brand-name">TR Ingotvale</div>
    <div class="contact-line">4870 Larkmere Parkway, Suite 800, Bellcastle, TX 75019 | www.tringotvale.com</div>
    <div class="band-gray"></div>
    <div class="band-blue"></div>
  </div>
</body>
</html>
```